New Business Card Needed

I need a new business card for Meridale Kitchen & Bath.
Logo is attached as well a my photo. Note: Make the logo Navy Blue.
Here is the text:
Gregory Tenwick
GC/Owner
Larkmoor VT
704-555-0139
gregory@meridaleHVX.com
www.meridaleHVX.com
Tag line on card: STYLE | UTILITY | ON SCHEDULE | IN SCOPE
Trim size: 2.56" X 2.56"
This is where we aim to cut the cards.
Safe area: 2.4" X 2.4"
Make sure any important aspects of your design such as text and logos are inside of the safe area, otherwise they may be cut off.
Bleed area: 2.71 X 2.71
Make sure that your background extends to fill the bleed to avoid your Business Cards having white edges when trimmed.
On the back side. Use photo of kitchen attached.

```html
<!DOCTYPE html>
<html lang="en">
<head>
<meta charset="utf-8">
<title>Meridale Kitchen &amp; Bath – Business Card</title>
<link href="https://fonts.googleapis.com/css2?family=Jost:wght@400;500;700&display=swap" rel="stylesheet">
<style>
  :root {
    --navy: #262a86;
    --paper: #ffffff;
    --stage: #f6c443;
    --photo-top: #e9e6e3;
    --photo-mid: #c9a57a;
    --photo-low: #8a5a3c;
    --portrait-bg: #3b3d42;
    --portrait-mid: #6f6259;
  }
  * { box-sizing: border-box; margin: 0; padding: 0; }
  html, body {
    width: 1200px; height: 782px; overflow: hidden;
    background: var(--stage);
    font-family: "Jost", "Futura", sans-serif;
    color: var(--navy);
  }
  .canvas { position: relative; width: 1200px; height: 782px; }
  .card {
    position: absolute; top: 171px; width: 440px; height: 440px;
    background: var(--paper);
    box-shadow: 0 14px 30px rgba(120, 80, 0, 0.25);
    overflow: hidden;
  }
  .card--back { left: 140px; }
  .card--front { left: 620px; }

  .kitchen-photo {
    position: absolute; inset: 0;
    background: linear-gradient(160deg, var(--photo-top) 0%, var(--photo-top) 30%, var(--photo-mid) 62%, var(--photo-low) 100%);
  }

  .brand {
    position: absolute; display: flex; align-items: center; gap: 10px;
    font-weight: 500; color: var(--navy); line-height: 1.05;
  }
  .brand__mark { width: 14px; height: 14px; background: var(--navy); flex: none; }
  .card--back .brand { left: 28px; top: 30px; font-size: 22px; }
  .card--front .brand { left: 34px; top: 40px; font-size: 30px; }
  .card--front .brand__mark { width: 18px; height: 18px; }

  .person { position: absolute; left: 34px; top: 150px; }
  .person__name { font-weight: 700; font-size: 27px; letter-spacing: 0.2px; line-height: 1.2; }
  .person__title { font-weight: 400; font-size: 17px; margin-top: 2px; line-height: 1.2; }
  .rule { position: absolute; left: 130px; top: 196px; width: 276px; height: 1.5px; background: var(--navy); }

  .portrait {
    position: absolute; right: 34px; top: 64px; width: 112px; height: 112px;
    background: radial-gradient(circle at 50% 55%, var(--portrait-mid) 0%, var(--portrait-bg) 70%);
  }

  .contacts { position: absolute; left: 34px; top: 218px; list-style: none; }
  .contacts li { display: flex; align-items: center; gap: 10px; font-size: 17px; height: 27px; }
  .contacts svg { width: 18px; height: 18px; flex: none; }

  .tagline {
    position: absolute; left: 34px; right: 34px; bottom: 40px;
    font-size: 15px; font-weight: 400; letter-spacing: 1px; white-space: nowrap;
  }
</style>
</head>
<body>
<main class="canvas">

  <section class="card card--back" aria-label="Card back">
    <div class="kitchen-photo" role="img" aria-label="Photo of a bright kitchen with wood cabinets, white marble island and pendant lights"></div>
    <div class="brand"><span class="brand__mark"></span><span>Meridale<br>Kitchen &amp; Bath</span></div>
  </section>

  <section class="card card--front" aria-label="Card front">
    <div class="brand"><span class="brand__mark"></span><span>Meridale<br>Kitchen &amp; Bath</span></div>

    <div class="portrait" role="img" aria-label="Portrait photo of Gregory Tenwick"></div>

    <div class="person">
      <p class="person__name">Gregory Tenwick</p>
      <p class="person__title">GC/Owner</p>
    </div>
    <div class="rule"></div>

    <ul class="contacts">
      <li>
        <svg viewBox="0 0 18 18" aria-hidden="true"><rect width="18" height="18" rx="3" fill="var(--navy)"/><path d="M5 5.5c0-.6.5-1 1-1h1.3l.9 2.3-1 .8a6 6 0 0 0 3.2 3.2l.8-1 2.3.9V12c0 .6-.4 1-1 1A8 8 0 0 1 5 5.5z" fill="#fff"/></svg>
        704-555-0139
      </li>
      <li>
        <svg viewBox="0 0 18 18" aria-hidden="true"><rect width="18" height="18" rx="3" fill="var(--navy)"/><rect x="4" y="5.5" width="10" height="7" fill="none" stroke="#fff" stroke-width="1.3"/><path d="M4 5.5l5 4 5-4" fill="none" stroke="#fff" stroke-width="1.3"/></svg>
        gregory@meridaleHVX.com
      </li>
      <li>
        <svg viewBox="0 0 18 18" aria-hidden="true"><rect width="18" height="18" rx="3" fill="var(--navy)"/><circle cx="9" cy="9" r="5" fill="none" stroke="#fff" stroke-width="1.3"/><path d="M4 9h10M9 4c-2 2.8-2 7.2 0 10M9 4c2 2.8 2 7.2 0 10" fill="none" stroke="#fff" stroke-width="1"/></svg>
        www.meridaleHVX.com
      </li>
      <li>
        <svg viewBox="0 0 18 18" aria-hidden="true"><rect width="18" height="18" rx="3" fill="var(--navy)"/><path d="M9 14.5s-4-4-4-7a4 4 0 0 1 8 0c0 3-4 7-4 7z" fill="#fff"/><circle cx="9" cy="7.5" r="1.5" fill="var(--navy)"/></svg>
        Larkmoor VT
      </li>
    </ul>

    <p class="tagline">STYLE | UTILITY | ON SCHEDULE | IN SCOPE</p>
  </section>

</main>
</body>
</html>
```